Stationery Design Project

Fire and building compliance company needs business card, letterhead and complement slip designed.
Have included a brief about business card, basic want front keep quite clean with just the MAS logo and the words Marbeck Alarm and Safety 2012 Ltd (small print) along the bottom. Website needs to be included (www.masalarm.example.nz) on either front or back.
The info for back is as per attachment.
Letterhead and complement slip should have the usual stuff MAS logo etc and also the accredited test lab logo at the bottom (can be small size)
Target Market(s)
Property owners, buisness managers
Industry/Entity Type
Building
Look and feel

```html
<!DOCTYPE html>
<html lang="en">
<head>
<meta charset="utf-8">
<title>Marbeck Alarm and Safety – Business Card Back</title>
<link rel="stylesheet" href="https://fonts.googleapis.com/css2?family=Arimo:wght@400;700&display=swap">
<style>
  :root {
    --blue-1: #168bd3;
    --blue-2: #2f9ad6;
    --blue-3: #45a9db;
    --blue-4: #36ade3;
    --blue-5: #33b8ea;
    --blue-6: #46c3ef;
    --blue-7: #5fcdf3;
    --blue-8: #83d7f5;
    --blue-9: #a9e3f8;
    --name-blue: #1a70a8;
    --ink: #111111;
    --grey-text: #555555;
    --paper: #ffffff;
    --accent-warm: rgba(240, 130, 60, 0.20);
    --accent-red: rgba(225, 80, 70, 0.12);
    --accent-cool: rgba(60, 150, 200, 0.20);
  }
  * { margin: 0; padding: 0; box-sizing: border-box; }
  html, body {
    width: 1200px;
    height: 685px;
    overflow: hidden;
    background: var(--paper);
  }
  .card {
    position: relative;
    width: 1200px;
    height: 685px;
    background: var(--paper);
    overflow: hidden;
    font-family: "Arimo", Arial, sans-serif;
  }
  .top-band {
    position: absolute;
    top: 0; left: 0;
    width: 1200px;
    height: 37px;
    display: flex;
  }
  .top-band span { flex: 1; }
  .top-band span:nth-child(1) { background: var(--blue-1); }
  .top-band span:nth-child(2) { background: var(--blue-2); }
  .top-band span:nth-child(3) { background: var(--blue-3); }
  .top-band span:nth-child(4) { background: var(--blue-4); }
  .top-band span:nth-child(5) { background: var(--blue-5); }
  .top-band span:nth-child(6) { background: var(--blue-6); }
  .top-band span:nth-child(7) { background: var(--blue-7); }
  .top-band span:nth-child(8) { background: var(--blue-8); }
  .top-band span:nth-child(9) { background: var(--blue-9); }

  .brand-watermark {
    position: absolute;
    left: 600px;
    top: 37px;
    width: 600px;
    height: 648px;
    background:
      radial-gradient(ellipse 46% 42% at 45% 38%, var(--accent-warm), transparent 72%),
      radial-gradient(ellipse 30% 30% at 22% 62%, var(--accent-red), transparent 72%),
      radial-gradient(ellipse 52% 38% at 72% 80%, var(--accent-cool), transparent 72%);
  }

  .person-name {
    position: absolute;
    left: 44px;
    top: 252px;
    font-size: 114px;
    font-weight: 700;
    line-height: 1;
    letter-spacing: -5px;
    white-space: nowrap;
  }
  .person-name .first { color: var(--name-blue); }
  .person-name .last { color: var(--ink); }

  .name-rule {
    position: absolute;
    left: 0;
    top: 360px;
    width: 620px;
    height: 8px;
    background: radial-gradient(ellipse 50% 50% at 45% 0%, rgba(0,0,0,0.22), transparent 100%);
  }

  .company {
    position: absolute;
    left: 65px;
    top: 369px;
    font-size: 35px;
    color: var(--grey-text);
    white-space: nowrap;
  }

  .contact {
    position: absolute;
    left: 65px;
    top: 442px;
    font-size: 25px;
    line-height: 31.5px;
    color: var(--grey-text);
    font-style: normal;
    white-space: nowrap;
  }

  .services {
    position: absolute;
    left: 697px;
    top: 183px;
    color: var(--ink);
  }
  .services-title {
    font-size: 26.8px;
    font-weight: 400;
    letter-spacing: -0.3px;
    margin-bottom: 57px;
  }
  .services-list { list-style: none; }
  .services-list li {
    font-size: 22.3px;
    line-height: 47.8px;
    letter-spacing: -0.5px;
    white-space: nowrap;
  }
</style>
</head>
<body>
  <main class="card">
    <div class="top-band" aria-hidden="true">
      <span></span><span></span><span></span><span></span><span></span><span></span><span></span><span></span><span></span>
    </div>

    <div class="brand-watermark" role="img" aria-label="Large faint company brand mark used as background decoration"></div>

    <h1 class="person-name"><span class="first">John</span><span class="last">DOE</span></h1>
    <div class="name-rule" aria-hidden="true"></div>

    <p class="company">Marbeck Alarm and Safety</p>

    <address class="contact">
      14 Kestrel Lane Extension,<br>
      Ridgeford, 4510<br>
      Phone: 06 555 0142<br>
      Fax: 06 555 0187<br>
      Email: admin@masalarm.example.nz
    </address>

    <section class="services">
      <h2 class="services-title">OUR SERVICES</h2>
      <ul class="services-list">
        <li>Building compliance specialists</li>
        <li>Building warrant of fitness preparation</li>
        <li>Fire alarms, Fire Extinguishers &amp; emergency lighting</li>
        <li>Approved evacuation schemes</li>
        <li>Pressure testing LPG CNG Fire extinguishers</li>
        <li>Security alarm and CCTV systems</li>
      </ul>
    </section>
  </main>
</body>
</html>
```